Rollin’ Kites Copper Tide beer can design

We are not looking for a new logo, we want to use our current logo!! Current Logo is Attached. We want to incorporate our current logo into a full can design for our new non-alcoholic, THC infused Beer design. We cannot use animals or cartoons. We also can not say beer. We would like to use our main label found at www.rollinkites-example.com
Several ideas include having small images of beer cans and beer mugs all over the can as a background. Another idea is to make it freedom and liberty themed. We want to make sure people understand it is a beer, even though we can say beer on the can.

Target Market(s)

30-50 year olds

Industry/Entity Type

THC beverage

Logo Text

Rollin’ Kites Copper Tide

Colors
59FF00
82FF00
B8FF75
E3FFCB
F4FFEA

Requirements
Must have
• Full 12 oz beer can design
Should not have
• No word beer, do not need a new logo, need a can design

```html
<!DOCTYPE html>
<html lang="en">
<head>
<meta charset="utf-8">
<title>Rollin’ Kites Copper Tide – Can Label</title>
<link href="https://fonts.googleapis.com/css2?family=Oswald:wght@500;700&display=swap" rel="stylesheet">
<style>
  :root {
    --page: #e6e4e5;
    --green-light: #9be85a;
    --green-mid: #4cc21f;
    --green-band: #36a91c;
    --green-deep: #23941a;
    --green-dark: #176f12;
    --ink: #1d1d1d;
    --white: #ffffff;
  }
  html, body {
    margin: 0;
    width: 1200px;
    height: 1200px;
    overflow: hidden;
    background: var(--page);
  }
  .can-label {
    position: absolute;
    left: 330px;
    top: 90px;
    width: 540px;
    height: 1020px;
    border-radius: 14px;
    overflow: hidden;
    background: var(--green-mid);
    font-family: "Oswald", sans-serif;
    box-shadow: 0 10px 30px rgba(0,0,0,0.12);
  }
  .label-pattern {
    position: absolute;
    left: 0; top: 0;
    width: 100%;
    height: 560px;
    background:
      radial-gradient(ellipse 60% 30% at 20% 12%, rgba(40,150,20,0.35), transparent 70%),
      radial-gradient(ellipse 50% 28% at 82% 30%, rgba(40,150,20,0.30), transparent 70%),
      radial-gradient(ellipse 55% 25% at 30% 88%, rgba(40,150,20,0.30), transparent 70%),
      radial-gradient(ellipse 45% 25% at 78% 86%, rgba(40,150,20,0.28), transparent 70%),
      linear-gradient(90deg, var(--green-mid) 0%, var(--green-light) 50%, var(--green-mid) 100%);
  }
  .brand-mark {
    position: absolute;
    left: 50%;
    top: 110px;
    transform: translateX(-50%);
    width: 340px;
    height: 340px;
    border-radius: 50%;
    background: var(--white);
    display: flex;
    align-items: center;
    justify-content: center;
    text-align: center;
  }
  .brand-name {
    margin: 0;
    font-weight: 700;
    font-size: 46px;
    line-height: 1.05;
    text-transform: uppercase;
    color: var(--ink);
  }
  .title-band {
    position: absolute;
    left: 0; top: 560px;
    width: 100%;
    height: 186px;
    background: var(--green-band);
    border-top: 8px solid var(--white);
    border-bottom: 8px solid var(--white);
    box-sizing: border-box;
    display: flex;
    align-items: center;
    justify-content: center;
  }
  .product-title {
    margin: 0;
    font-weight: 700;
    font-size: 60px;
    line-height: 1.1;
    text-transform: uppercase;
    color: var(--white);
    text-align: center;
  }
  .description-panel {
    position: absolute;
    left: 0; top: 746px;
    width: 100%;
    height: 274px;
    background:
      radial-gradient(ellipse 45% 30% at 25% 30%, rgba(255,255,255,0.05), transparent 70%),
      radial-gradient(ellipse 45% 30% at 80% 60%, rgba(255,255,255,0.05), transparent 70%),
      linear-gradient(180deg, var(--green-deep) 0%, var(--green-dark) 100%);
  }
  .description-text {
    position: absolute;
    left: 50%;
    top: 36px;
    transform: translateX(-50%);
    margin: 0;
    width: 410px;
    font-weight: 700;
    font-size: 23px;
    line-height: 1.6;
    color: var(--white);
    text-align: center;
  }
</style>
</head>
<body>
  <div class="can-label">
    <div class="label-pattern" role="img" aria-label="Scattered pattern of small cans, mugs and leaves in lighter and darker greens"></div>
    <div class="brand-mark">
      <p class="brand-name">Rollin’ Kites<br>Beverages</p>
    </div>
    <div class="title-band">
      <h1 class="product-title">Rollin’ Kites<br>Copper Tide</h1>
    </div>
    <div class="description-panel" role="img" aria-label="Faint pattern of small cans, mugs and leaves on dark green">
      <p class="description-text">Lorem ipsum dolor sit amet, consectetur adipiscing elit. Duis accumsan mollis hendrerit. Nunc quis placerat lectus, vel finibus metus. Aenean a nunc risus.</p>
    </div>
  </div>
</body>
</html>
```